Business Card Design

We are a project managment company specializing in Interior fitout
PVH is for Commercial, Domestic, Industial - we provide managment to these industries and see the projects through design to contruction
Would like an area on the back of the card where peoplr can write notes
Thinking laser lines and architectural finishes
Colour theme at the moment is light grey and red although im open to any colour/design scheme

Industry/Entity Type

Business

Contact Information for Business Card

PVH Ventures
Brett Lamonte
Managing Director
0487215694
brett@pvhventures-example.com.au

```html
<!DOCTYPE html>
<html lang="en">
<head>
<meta charset="utf-8">
<title>Corvane Projects — Business Card</title>
<link rel="stylesheet" href="https://fonts.googleapis.com/css2?family=Lato:wght@300;400;700&display=swap">
<style>
  :root {
    --bg: #d9d9d9;
    --card: #f4f4f4;
    --card-edge: #e2e2e2;
    --ink-dark: #4a4a4a;
    --ink-mid: #7b7b7b;
    --rule: #b9b9b9;
    --red: #d3262e;
    --red-soft: #e25a4a;
    --band-grey: #a9a9a9;
    --faint: #e6e6e6;
  }
  * { box-sizing: border-box; margin: 0; padding: 0; }
  html, body { width: 1200px; height: 1200px; overflow: hidden; }
  body {
    background: var(--bg);
    font-family: "Lato", Arial, sans-serif;
    position: relative;
  }
  .card {
    position: absolute;
    width: 680px;
    height: 390px;
    background: linear-gradient(135deg, #fafafa 0%, var(--card) 55%, var(--card-edge) 100%);
    box-shadow: 0 10px 24px rgba(0,0,0,0.18);
    overflow: hidden;
  }
  .card-back { left: 60px; top: 60px; }
  .card-front { left: 460px; top: 500px; }

  .brand { display: flex; align-items: center; gap: 12px; position: absolute; white-space: nowrap; }
  .brand-dot {
    width: 30px; height: 30px; border-radius: 50%;
    background: var(--ink-mid); flex: none;
  }
  .brand-name {
    font-weight: 400; color: var(--ink-dark);
    letter-spacing: 0.08em; text-transform: uppercase;
  }
  .card-back .brand { left: 50px; top: 128px; }
  .card-back .brand-name { font-size: 22px; }

  .notes-lines { position: absolute; left: 410px; top: 70px; width: 230px; z-index: 1; }
  .notes-lines span { display: block; height: 1px; background: var(--rule); margin-bottom: 46px; }

  .faint-disc {
    position: absolute; right: -60px; bottom: -90px;
    width: 260px; height: 260px; border-radius: 50%;
    background: var(--faint);
  }

  .card-front .brand { left: 60px; top: 84px; }
  .card-front .brand-dot { width: 34px; height: 34px; }
  .card-front .brand-name { font-size: 32px; }

  .person { position: absolute; right: 80px; top: 150px; text-align: right; }
  .person-name { font-size: 26px; font-weight: 700; color: var(--ink-dark); }
  .person-role { font-size: 17px; font-weight: 400; color: var(--red-soft); margin-top: 2px; }

  .edge-tab {
    position: absolute; right: 0; top: 150px;
    width: 18px; height: 36px; background: var(--red);
    border-radius: 8px 0 0 8px;
  }

  .divider { position: absolute; left: 60px; top: 240px; width: 470px; height: 1px; background: var(--rule); }

  .contact { position: absolute; left: 60px; top: 262px; list-style: none; }
  .contact li {
    display: flex; align-items: center; gap: 14px;
    font-size: 18px; color: var(--ink-dark); margin-bottom: 10px;
  }
  .contact svg { width: 18px; height: 18px; flex: none; }

  .card-bands { position: absolute; left: 0; bottom: 0; width: 680px; height: 80px; }

  .lockup { position: absolute; right: 50px; top: 1050px; }
  .lockup .brand { position: static; gap: 18px; }
  .lockup .brand-dot { width: 56px; height: 56px; }
  .lockup .brand-name { font-size: 40px; }
</style>
</head>
<body>

  <section class="card card-back" aria-label="Card back with notes area">
    <div class="brand">
      <span class="brand-dot"></span>
      <span class="brand-name">Corvane Projects</span>
    </div>
    <div class="faint-disc"></div>
    <div class="notes-lines">
      <span></span><span></span><span></span><span></span><span></span><span></span>
    </div>
  </section>

  <section class="card card-front" aria-label="Card front">
    <div class="brand">
      <span class="brand-dot"></span>
      <span class="brand-name">Corvane Projects</span>
    </div>

    <div class="edge-tab"></div>
    <div class="person">
      <p class="person-name">Brett Lamonte</p>
      <p class="person-role">Managing Director</p>
    </div>

    <div class="divider"></div>

    <ul class="contact">
      <li>
        <svg viewBox="0 0 18 18" aria-hidden="true"><rect x="4" y="1" width="10" height="16" rx="2" fill="none" stroke="#555" stroke-width="1.6"/><circle cx="9" cy="14" r="1" fill="#555"/></svg>
        +33 048 72 15 694
      </li>
      <li>
        <svg viewBox="0 0 18 18" aria-hidden="true"><rect x="1" y="4" width="16" height="11" fill="#555"/><path d="M1 4 L9 10 L17 4" fill="none" stroke="#f4f4f4" stroke-width="1.4"/></svg>
        brett@corvaneprojects-example.com.au
      </li>
    </ul>

    <svg class="card-bands" viewBox="0 0 680 80" aria-hidden="true">
      <polygon points="470,10 680,10 680,80 0,80 0,62 450,62" fill="var(--band-grey)"/>
      <polygon points="0,54 450,54 470,42 470,50 454,60 0,60" fill="var(--red)"/>
      <rect x="0" y="66" width="680" height="14" fill="#c3c3c3"/>
    </svg>
  </section>

  <div class="lockup">
    <div class="brand">
      <span class="brand-dot"></span>
      <span class="brand-name">Corvane Projects</span>
    </div>
  </div>

</body>
</html>
```